Pathwell | An Alcolohism Recovery Blogging Site

Pathwell.com.au is a blog based on alcoholism. Primarily, alcholics who are in sobreity, or recovery. The blog posts are centred around this and are written by other alcholics who share their thoughts, strenght, experience, thoeries on how to get sober, and stay sober, but primarily, live a better life in active sobriety. The site provides information related to CR and other services/groups that assist in alcolohism. We write E-Books and sell these also. Pathwell strives to be a blog that alcoholics want to read, and get strength and hope from reading it, and the posts from other users. We want to be easy to use, simple to navigate and sharply designed. We want the site to be cutting edge and appealing. We want to engage the audience from the first moment they hit the page, no matter where they land. I like this website as a model for a wordpress site making good use of simplicity = thriftlane.com.au

Target Market(s)

People who might think they have a problem with Alcohol, people who are alcholics looking at entering rehab or recovery, people that are alcoholics in recovery already

Requirements
Must have
• simplicity, large fonts for headings, space for advertising through ad words and other forms, nice large navigation across the top, a sharp, html 5 feel, i want to be using great fonts and nice/sheek.
Nice to have
• logo will be used in print as well as online. It would be VERY GOOD to have someone design a ecover for my ebook i will be selling on this website. the book is titled "THE CLEAR MORNING PROMISE - The Gentle Path to finding calm and keeping it for good!"
Should not have
• do not include illustrations of alcohol.

```html
<!DOCTYPE html>
<html lang="en">
<head>
<meta charset="utf-8">
<title>Pathwell | Alcoholism Recovery Blog</title>
<link rel="stylesheet" href="https://fonts.googleapis.com/css2?family=Roboto+Condensed:wght@400;700&family=Gelasio:wght@400;700&family=Arimo:wght@400;700&family=Open+Sans:wght@400;600&display=swap">
<style>
:root{
  --sky-top:#a9d6ec;
  --sky-bottom:#d5ecf7;
  --nav-bar:#8fcbe6;
  --navy:#0b3d73;
  --navy-deep:#003a75;
  --ink:#1f2a36;
  --heading:#1d4f7c;
  --grey-head:#3a4650;
  --panel:#fbf9f7;
  --white:#ffffff;
  --line:#2d6ea6;
  --side:#76c7e6;
  --side-head:#0f3c66;
  --btn-top:#4aa3d6;
  --btn-bottom:#1869a8;
  --link:#1d5a96;
  --border:#e3e3e3;
}
*{box-sizing:border-box;margin:0;padding:0}
html,body{width:707px;height:1200px;overflow:hidden}
body{position:relative;background:var(--white);font-family:"Arimo",Arial,sans-serif;color:var(--ink)}
.abs{position:absolute}

.masthead{left:0;top:0;width:707px;height:340px;background:linear-gradient(180deg,var(--sky-top) 0%,#bfe2f3 40%,var(--sky-bottom) 100%)}
.brand{left:14px;top:50px;display:flex;align-items:center;gap:8px;font-family:"Roboto Condensed",sans-serif;font-weight:700;font-size:30px;color:var(--grey-head)}
.brand-mark{width:14px;height:14px;background:var(--navy)}
.ad-slot{background:var(--white);border:1px solid #555;display:flex;align-items:center;justify-content:center;font-family:"Gelasio",Georgia,serif;font-size:22px;color:#111}
.ad-top{left:200px;top:16px;width:494px;height:81px}
.ad-bottom{left:13px;top:1059px;width:680px;height:75px;border-color:var(--border)}

.main-nav{left:0;top:116px;width:707px;height:35px;background:linear-gradient(180deg,#a5d8ee,var(--nav-bar));display:flex;align-items:center;padding-left:12px;font-family:"Roboto Condensed",sans-serif;font-weight:700;font-size:13.5px}
.main-nav a{color:var(--navy);text-decoration:none;margin-right:22px}
.main-nav a.current{background:linear-gradient(180deg,#fff,#cfd6da);border-radius:3px;padding:2px 17px;margin-right:20px;box-shadow:0 1px 2px rgba(0,0,0,.3)}
.search{left:533px;top:126px;width:123px;height:16px;background:var(--white);border:1px solid #b7c6cf;font-size:7.5px;color:#9aa;padding:3px 4px}
.search-icon{left:664px;top:124px}

.hero{left:13px;top:151px;width:680px;height:255px;background:var(--panel);box-shadow:0 2px 6px rgba(0,0,0,.12)}
.welcome{left:28px;top:182px;font-family:"Roboto Condensed",sans-serif;font-weight:700;font-size:24px;color:var(--heading)}
.welcome b{color:var(--grey-head)}
.welcome-rule{left:28px;top:217px;width:282px;border-top:1px dashed #555}
.welcome-text{left:28px;top:227px;width:282px;font-size:7.4px;line-height:11.2px;color:#222}
.btn{display:inline-flex;align-items:center;justify-content:center;gap:4px;color:var(--white);font-weight:700;background:linear-gradient(180deg,var(--btn-top),var(--btn-bottom));border:1px solid #135c92}
.btn-large{left:28px;top:315px;width:104px;height:25px;font-family:"Roboto Condensed",sans-serif;font-size:12px}
.follow{left:28px;top:366px;font-family:"Roboto Condensed",sans-serif;font-weight:700;font-size:16px;color:var(--navy);display:flex;align-items:center;gap:2px}
.social{top:360px;width:33px;height:33px;border-radius:4px}
.s1{left:126px;background:#3b5a9a}.s2{left:168px;background:#5ec2e4}.s3{left:210px;background:#0c5b8a}.s4{left:252px;background:#e2731d}

.photo-frame{left:326px;top:166px;width:328px;height:196px;background:var(--white);box-shadow:0 1px 4px rgba(0,0,0,.3)}
.photo{left:332px;top:172px;width:316px;height:186px;background:linear-gradient(160deg,#5d7283 0%,#9fb0bd 55%,#d9dfe3 100%)}
.photo-caption{left:309px;top:360px;width:361px;height:33px;background:var(--navy);color:var(--white);font-family:"Open Sans",sans-serif;font-size:12.5px;display:flex;align-items:center;justify-content:center}

.posts{left:13px;top:419px;width:530px;height:625px;background:var(--white);border:1px solid var(--border)}
.post{position:absolute;left:10px;width:502px}
.post-title{font-family:"Gelasio",Georgia,serif;font-size:13.5px;color:var(--heading);font-weight:400}
.post-meta{display:flex;justify-content:space-between;font-size:7.4px;color:#444;margin-top:2px;padding-bottom:6px;border-bottom:1px dashed var(--line)}
.post-meta b{color:var(--link)}
.post-body{font-size:6.9px;line-height:12.1px;margin-top:6px;height:112px;border-bottom:1px dashed var(--line);padding-bottom:4px;color:#222}
.post-actions{margin-top:12px;display:flex;gap:5px}
.btn-small{height:16px;padding:0 8px;font-size:7.6px}
.more-posts{left:10px;top:597px;height:17px;font-size:7.6px;padding:0 8px}

.ebook{left:553px;top:419px;width:141px;height:121px}
.ebook-cover{left:0;top:0;width:104px;height:121px;background:linear-gradient(180deg,#f4b248 0%,#ee9a37 60%,#6b3a1c 100%)}
.ebook-title{left:6px;top:88px;width:96px;font-family:"Roboto Condensed",sans-serif;font-weight:700;font-size:10.5px;line-height:12px;color:var(--white);text-align:center}
.ebook-tab{left:108px;top:0;width:33px;height:121px;background:#f7b52a;display:flex;flex-direction:column;align-items:center;padding-top:6px}
.ebook-tab span{writing-mode:vertical-rl;font-family:"Roboto Condensed",sans-serif;font-weight:700;font-size:15px;color:#222;letter-spacing:1px}

.widget{left:552px;width:142px;background:var(--side);padding:12px 10px 0 14px}
.widget h3{font-family:"Roboto Condensed",sans-serif;font-weight:700;font-size:13px;color:var(--side-head);padding-bottom:5px;border-bottom:1px solid #a9dcf0;margin-bottom:5px}
.widget li{list-style:none;font-size:7.4px;font-weight:700;color:var(--side-head);padding-left:8px;position:relative;line-height:14px}
.widget li::before{content:"";position:absolute;left:0;top:4px;border-left:5px solid var(--white);border-top:3px solid transparent;border-bottom:3px solid transparent}
.recent li{font-weight:400;text-decoration:underline;color:var(--link);line-height:9px;margin-bottom:6px}
.recent li::before{top:2px}

.site-footer{left:0;top:1145px;width:707px;height:55px;background:var(--navy-deep);color:var(--white);font-size:7.4px;text-align:center;padding-top:16px;line-height:13px}
</style>
</head>
<body>
<header class="abs masthead"></header>
<div class="abs brand"><span class="brand-mark"></span>Pathwell</div>
<div class="abs ad-slot ad-top">Ad Space</div>

<nav class="abs main-nav">
  <a class="current">Home</a><a>About Us</a><a>Latest Post</a><a>Success Story</a><a>E-Book</a><a>Blogs</a><a>Contact Us</a>
</nav>
<div class="abs search">Type your search here</div>
<svg class="abs search-icon" width="20" height="20" viewBox="0 0 20 20"><circle cx="8" cy="8" r="5.5" fill="none" stroke="#1a2a3a" stroke-width="2.2"/><line x1="12" y1="12" x2="18" y2="18" stroke="#1a2a3a" stroke-width="3" stroke-linecap="round"/></svg>

<section class="abs hero"></section>
<h1 class="abs welcome">welcome to <b>Pathwell</b></h1>
<div class="abs welcome-rule"></div>
<p class="abs welcome-text">Lorem ipsum dolor sit amet, consectetur adipiscing elit. Maecenas at nulla ut eros interdum bibendum nec nec urna. Nullam condimentum malesuada mauris eget mattis. Vivamus facilisis diam non diam aliquet id vestibulum mauris viverra. Praesent mollis, sem eu venenatis sollicitudin, erat libero convallis tellus, quis sagittis velit lectus et diam. Praesent eu nisl eget elit mollis iaculis quis ullamcorper ante.</p>
<a class="abs btn btn-large">Read More <svg width="20" height="8" viewBox="0 0 20 8"><path d="M1 1l3 3-3 3M7 1l3 3-3 3M13 1l3 3-3 3" fill="none" stroke="#fff" stroke-width="1.8"/></svg></a>
<div class="abs follow">Follow Us <svg width="28" height="38" viewBox="0 0 28 38"><path d="M0 10h12V0l16 19-16 19V28H0z" fill="#0b3d73"/><text x="2" y="24" font-family="Roboto Condensed, sans-serif" font-weight="700" font-size="13" fill="#fff">On</text></svg></div>
<div class="abs social s1" role="img" aria-label="Social profile link"></div>
<div class="abs social s2" role="img" aria-label="Social profile link"></div>
<div class="abs social s3" role="img" aria-label="Social profile link"></div>
<div class="abs social s4" role="img" aria-label="News feed link"></div>

<div class="abs photo-frame"></div>
<div class="abs photo" role="img" aria-label="Photo of a businessman sprinting forward from a starting line under a cloudy sky"></div>
<div class="abs photo-caption">We Help You To Recover Yourself From Alcoholism</div>

<main class="abs posts">
  <article class="post" style="top:24px">
    <h2 class="post-title">Lorem ipsum dolor sit amet</h2>
    <div class="post-meta"><span><b>posted :</b> 16-08-2010 By Mr Tom Hale, Geelong</span><span><b>Category :</b> General &nbsp;&nbsp;|&nbsp;&nbsp; <b>Comments :</b> 02</span></div>
    <p class="post-body">Lorem ipsum dolor sit amet, consectetur adipiscing elit. Ut aliquet lacus et dolor mollis bibendum. Mauris sodales magna vel erat porttitor vel hendrerit velit lacinia. Vestibulum neque libero, placerat eget sagittis vel, vulputate eget lectus. Nullam tortor libero, dapibus tempus elementum id, feugiat vel odio. Proin in orci quis ipsum hendrerit mattis. Nullam lectus odio, venenatis at laoreet non, consectetur id massa. Vestibulum tempor porta volutpat. Nunc quis velit sem, et euismod nunc. Maecenas arcu tellus, viverra in scelerisque id, tristique eu massa. Curabitur scelerisque, urna suscipit inter-dum pretium, tortor nisl adipiscing lorem, quis pharetra metus orci at elit. Quisque auctor fringilla imperdiet. Maecenas sodales, erat quis sollicitudin aliquam, eros arcu fringilla mauris, sit amet tincidunt sapien quam id arcu. Nunc vitae nunc enim. Nam libero eros, pellentesque vel laoreet vitae, consequat consequat libero.</p>
    <div class="post-actions"><a class="btn btn-small">Read More &raquo;</a><a class="btn btn-small">Comments &raquo;</a></div>
  </article>
  <article class="post" style="top:219px">
    <h2 class="post-title">Lorem ipsum dolor sit amet</h2>
    <div class="post-meta"><span><b>posted :</b> 16-08-2010 By Mr Tom Hale, Geelong</span><span><b>Category :</b> General &nbsp;&nbsp;|&nbsp;&nbsp; <b>Comments :</b> 02</span></div>
    <p class="post-body">Lorem ipsum dolor sit amet, consectetur adipiscing elit. Ut aliquet lacus et dolor mollis bibendum. Mauris sodales magna vel erat porttitor vel hendrerit velit lacinia. Vestibulum neque libero, placerat eget sagittis vel, vulputate eget lectus. Nullam tortor libero, dapibus tempus elementum id, feugiat vel odio. Proin in orci quis ipsum hendrerit mattis. Nullam lectus odio, venenatis at laoreet non, consectetur id massa. Vestibulum tempor porta volutpat. Nunc quis velit sem, et euismod nunc. Maecenas arcu tellus, viverra in scelerisque id, tristique eu massa. Curabitur scelerisque, urna suscipit inter-dum pretium, tortor nisl adipiscing lorem, quis pharetra metus orci at elit. Quisque auctor fringilla imperdiet. Maecenas sodales, erat quis sollicitudin aliquam, eros arcu fringilla mauris, sit amet tincidunt sapien quam id arcu. Nunc vitae nunc enim. Nam libero eros, pellentesque vel laoreet vitae, consequat consequat libero.</p>
    <div class="post-actions"><a class="btn btn-small">Read More &raquo;</a><a class="btn btn-small">Comments &raquo;</a></div>
  </article>
  <article class="post" style="top:413px">
    <h2 class="post-title">Lorem ipsum dolor sit amet</h2>
    <div class="post-meta"><span><b>posted :</b> 16-08-2010 By Mr Tom Hale, Geelong</span><span><b>Category :</b> General &nbsp;&nbsp;|&nbsp;&nbsp; <b>Comments :</b> 02</span></div>
    <p class="post-body">Lorem ipsum dolor sit amet, consectetur adipiscing elit. Ut aliquet lacus et dolor mollis bibendum. Mauris sodales magna vel erat porttitor vel hendrerit velit lacinia. Vestibulum neque libero, placerat eget sagittis vel, vulputate eget lectus. Nullam tortor libero, dapibus tempus elementum id, feugiat vel odio. Proin in orci quis ipsum hendrerit mattis. Nullam lectus odio, venenatis at laoreet non, consectetur id massa. Vestibulum tempor porta volutpat. Nunc quis velit sem, et euismod nunc. Maecenas arcu tellus, viverra in scelerisque id, tristique eu massa. Curabitur scelerisque, urna suscipit inter-dum pretium, tortor nisl adipiscing lorem, quis pharetra metus orci at elit. Quisque auctor fringilla imperdiet. Maecenas sodales, erat quis sollicitudin aliquam, eros arcu fringilla mauris, sit amet tincidunt sapien quam id arcu. Nunc vitae nunc enim. Nam libero eros, pellentesque vel laoreet vitae, consequat consequat libero.</p>
    <div class="post-actions"><a class="btn btn-small">Read More &raquo;</a><a class="btn btn-small">Comments &raquo;</a></div>
  </article>
  <a class="abs btn more-posts">View More Posts &raquo;</a>
</main>

<aside class="abs ebook">
  <div class="abs ebook-cover" role="img" aria-label="E-book cover artwork showing two people shaking hands"></div>
  <div class="abs ebook-title">THE CLEAR MORNING PROMISE</div>
  <div class="abs ebook-tab"><span>BUY E BOOK</span>
    <svg width="16" height="16" viewBox="0 0 16 16" style="margin-top:6px"><circle cx="8" cy="8" r="7" fill="none" stroke="#e0601b" stroke-width="2"/><path d="M6 4l4 4-4 4" fill="none" stroke="#e0601b" stroke-width="2"/></svg>
  </div>
</aside>

<section class="abs widget recent" style="top:547px;height:119px">
  <h3>Recent Posts</h3>
  <ul><li>Lorem ipsum dolor sit amet nuno valencia</li><li>Lorem ipsum dolor sit amet nuno valencia</li><li>Lorem ipsum dolor sit amet nuno valencia</li></ul>
</section>
<section class="abs widget" style="top:675px;height:133px">
  <h3>Archieves</h3>
  <ul><li>August 2010</li><li>July 2010</li><li>June 2010</li><li>May 2010</li><li>April 2010</li><li>March 2010</li></ul>
</section>
<section class="abs widget" style="top:817px;height:104px">
  <h3>Categories</h3>
  <ul><li>Lorem ipsum</li><li>Lorem ipsum</li><li>Lorem ipsum</li><li>Lorem ipsum</li></ul>
</section>
<section class="abs widget" style="top:929px;height:117px">
  <h3>Meta</h3>
  <ul><li>Register</li><li>Log in</li><li>Entries RSS</li><li>Comments RSS</li><li>Pressbook.org</li></ul>
</section>

<div class="abs ad-slot ad-bottom">Ad Space</div>

<footer class="abs site-footer">
  Home &nbsp;&nbsp;|&nbsp;&nbsp; About Us &nbsp;&nbsp;|&nbsp;&nbsp; Latest Post &nbsp;&nbsp;|&nbsp;&nbsp; Success Story &nbsp;&nbsp;|&nbsp;&nbsp; E-Book &nbsp;&nbsp;|&nbsp;&nbsp; Blogs &nbsp;&nbsp;|&nbsp;&nbsp; Contact Us<br>
  &copy; Copyright Pathwell.com.au &nbsp;&nbsp;|&nbsp;&nbsp; All Rights Reserved
</footer>
</body>
</html>
```